Global Consulting firm needs a Business Card Design (Contest)

We need a business card design for a company with global reach called 'MapleRidge Group'. MapleRidge Group is a Trusted Procurement Advisor that consults for Pinnacle 300 and Vantage 800 companies to find cost reductions in their spending. We would like to see designs that communicate fiduciary trust and sense of partnership. The Front should have our logo w/ 'trusted procurement advisor', Employee name and title, company address, email, phone and fax (logo attached "Maple ridge group final"). The color scheme and basic concept should be consistent with our presentation front page (attached "MRG presentation cover page"). The Back should have our website (www.mridgellc.com) and an array of our areas of expertise: office supplies, lab supplies, wireless telecom, MRO and IT (see "lab supplies" file for example).

```html
<!DOCTYPE html>
<html lang="en">
<head>
<meta charset="utf-8">
<title>MapleRidge Group – Business Cards</title>
<link rel="stylesheet" href="https://fonts.googleapis.com/css2?family=Jost:ital,wght@0,400;0,500;1,400&family=Libre+Baskerville:ital,wght@0,700;1,700&display=swap">
<style>
  :root {
    --bg: #2a1a14;
    --card-light: #ebe8e4;
    --card-dark: #1c1c1c;
    --brown: #7a4a32;
    --rust: #9a5a3c;
    --gold: #c9a227;
    --gold-deep: #8a6a12;
    --ink-dark: #3a3430;
    --ink-light: #e8e4df;
    --rule-light: #cfcac4;
  }
  * { margin: 0; padding: 0; box-sizing: border-box; }
  html, body { width: 1200px; height: 700px; overflow: hidden; }
  body {
    background: var(--bg);
    font-family: "Jost", sans-serif;
    position: relative;
  }
  .card {
    position: absolute;
    top: 207px;
    width: 500px;
    height: 286px;
    border-radius: 3px;
    box-shadow: 0 10px 30px rgba(0,0,0,.45);
  }

  /* Back side */
  .card-back {
    left: 60px;
    background: var(--card-light);
    color: var(--ink-dark);
    text-align: center;
  }
  .card-back .mark {
    width: 44px; height: 44px;
    border-radius: 50%;
    background: radial-gradient(circle at 40% 35%, #e9cf5a, var(--gold) 55%, var(--gold-deep));
    margin: 34px auto 0;
  }
  .card-back .website {
    margin-top: 6px;
    font-size: 30px;
    letter-spacing: 1px;
    color: var(--ink-dark);
  }
  .card-back .rule {
    height: 4px;
    background: var(--brown);
    margin: 6px 0 12px;
  }
  .expertise {
    list-style: none;
    font-size: 16px;
    font-style: italic;
    line-height: 1.25;
  }

  /* Front side */
  .card-front {
    left: 640px;
    background: var(--card-dark);
    color: var(--ink-light);
  }
  .brand {
    position: absolute;
    top: 28px; left: 40px;
    display: flex; align-items: center; gap: 12px;
  }
  .brand .mark {
    width: 34px; height: 34px;
    border-radius: 50%;
    background: radial-gradient(circle at 40% 35%, #e9cf5a, var(--gold) 55%, var(--gold-deep));
  }
  .brand-name {
    font-family: "Libre Baskerville", serif;
    font-weight: 700;
    font-size: 28px;
    color: var(--ink-light);
  }
  .tagline {
    position: absolute;
    top: 70px; left: 150px;
    font-family: "Libre Baskerville", serif;
    font-style: italic;
    font-weight: 700;
    font-size: 15px;
    color: var(--ink-light);
  }
  .card-front .rule {
    position: absolute;
    top: 96px; left: 0; right: 0;
    height: 5px;
    background: var(--rule-light);
  }
  .person {
    position: absolute;
    top: 114px; left: 30px;
    font-size: 14px;
    line-height: 1.3;
  }
  .person .title { color: var(--rust); font-size: 12px; }
  .person .email { font-size: 13px; }
  .office {
    position: absolute;
    right: 30px; bottom: 30px;
    text-align: right;
    font-size: 17px;
    line-height: 1.25;
  }
  .office .address { font-weight: 500; margin-bottom: 2px; }
  .office .label { color: var(--rust); font-size: 14px; }
</style>
</head>
<body>

  <section class="card card-back" aria-label="Card back">
    <div class="mark"></div>
    <p class="website">www.mridgellc.com</p>
    <div class="rule"></div>
    <ul class="expertise">
      <li>Office supplies</li>
      <li>Lab supplies</li>
      <li>Wireless telecom</li>
      <li>MRO and IT</li>
    </ul>
  </section>

  <section class="card card-front" aria-label="Card front">
    <div class="brand">
      <div class="mark"></div>
      <span class="brand-name">MapleRidge Group</span>
    </div>
    <p class="tagline">Trusted Procurement Advisor</p>
    <div class="rule"></div>
    <div class="person">
      <p class="name">Daniel Harper</p>
      <p class="title">President</p>
      <p class="email">dharper@mridgellc.com</p>
    </div>
    <div class="office">
      <p class="address">Fairhaven, Ohio</p>
      <p><span class="label">Phone:</span> (800) 555 - 0142</p>
      <p><span class="label">Fax:</span> (555) 555 - 0187</p>
      <p><span class="label">E-Mail:</span> info@mridgellc.com</p>
    </div>
  </section>

</body>
</html>
```